Revamp Landing Page

Our current landing page is http://velvetdenkx.com/ and we're looking for our site to look like this http://www.goldparrotclub.com/. Classy, Sleek, Simple elegant.

The site should be desktop and mobile optimized.
Pages should be built out and the same structure. Drink Menu, Gallery, Events, Table Reservations, Membership, Press, Contact Us.

Feel free to use the images on our website.

```html
<!DOCTYPE html>
<html lang="en">
<head>
<meta charset="UTF-8">
<title>Velvet Den</title>
<link href="https://fonts.googleapis.com/css2?family=Open+Sans:wght@300;400;600;700&display=swap" rel="stylesheet">
<style>
  :root {
    --page-bg: #faf1ee;
    --frame-line: #cbbcb4;
    --ink: #2b2522;
    --muted-ink: #7a6a62;
    --gold: #c79b55;
    --gold-text: #c8974a;
    --band-bg: #f3e3dc;
    --footer-bg: #ffffff;
    --photo-dark: #3a2a2c;
    --photo-warm: #a5676a;
  }
  * { margin: 0; padding: 0; box-sizing: border-box; }
  html, body { width: 1200px; height: 780px; overflow: hidden; }
  body {
    position: relative;
    background: var(--page-bg);
    font-family: "Open Sans", Arial, sans-serif;
    color: var(--ink);
  }
  .brand {
    position: absolute; top: 34px; left: 0; width: 1200px;
    text-align: center;
    font-weight: 300; font-size: 44px; letter-spacing: 4px;
    color: var(--ink); line-height: 56px;
  }
  .frame-line { position: absolute; background: var(--frame-line); }
  .frame-top-left { left: 186px; top: 114px; width: 91px; height: 1px; }
  .frame-top-right { left: 922px; top: 114px; width: 91px; height: 1px; }
  .frame-left { left: 186px; top: 114px; width: 1px; height: 505px; }
  .frame-right { left: 1012px; top: 114px; width: 1px; height: 505px; }
  .frame-bottom-left { left: 186px; top: 619px; width: 159px; height: 1px; }
  .frame-bottom-right { left: 856px; top: 619px; width: 157px; height: 1px; }

  .main-nav {
    position: absolute; top: 107px; left: 0; width: 1200px;
    display: flex; justify-content: center; gap: 19px;
    font-size: 11px; letter-spacing: 1.3px; font-weight: 400;
  }
  .main-nav a { color: var(--ink); text-decoration: none; }

  .hero {
    position: absolute; left: 222px; top: 145px; width: 755px; height: 442px;
    background:
      linear-gradient(100deg, rgba(20,28,18,.85) 0%, rgba(40,35,30,.55) 28%, rgba(0,0,0,0) 50%),
      linear-gradient(180deg, #4a3440 0%, var(--photo-warm) 45%, #8a5a55 75%, var(--photo-dark) 100%);
  }
  .hero-copy { position: absolute; left: 52px; top: 270px; width: 260px; }
  .hero-title {
    color: var(--gold-text); font-weight: 700; font-size: 12px;
    line-height: 14.5px; text-transform: uppercase;
  }
  .hero-text { color: #fff; font-size: 10.2px; line-height: 12.5px; margin-top: 9px; }
  .hero-button {
    display: inline-block; margin-top: 25px;
    background: var(--gold); color: #fff; text-decoration: none;
    font-size: 10px; font-weight: 700; letter-spacing: 1.5px;
    width: 164px; height: 32px; line-height: 32px; text-align: center;
  }

  .social {
    position: absolute; top: 611px; left: 0; width: 1200px;
    display: flex; justify-content: center; gap: 14px;
    font-size: 10.2px; letter-spacing: 1.1px; color: var(--muted-ink);
  }
  .social a { color: var(--muted-ink); text-decoration: none; display: flex; align-items: center; gap: 8px; }
  .social-dot { width: 9px; height: 9px; border-radius: 50%; background: var(--muted-ink); }

  .party-band {
    position: absolute; left: 0; top: 667px; width: 1200px; height: 43px;
    background: var(--band-bg);
    display: flex; justify-content: center; align-items: center; gap: 6px;
    font-size: 12.5px;
  }
  .party-band a { color: var(--ink); font-weight: 700; text-decoration: underline; }

  .site-footer {
    position: absolute; left: 0; top: 710px; width: 1200px; height: 70px;
    background: var(--footer-bg);
    text-align: center; padding-top: 25px;
    font-size: 11px; letter-spacing: 1.2px; color: var(--ink);
  }
</style>
</head>
<body>
  <header>
    <div class="brand">VELVET DEN</div>
    <nav class="main-nav">
      <a href="#">DRINK MENU</a>
      <a href="#">GALLERY</a>
      <a href="#">EVENTS</a>
      <a href="#">TABLE RESERVATIONS</a>
      <a href="#">MEMBERSHIP</a>
      <a href="#">PRESS</a>
      <a href="#">CONTACT US</a>
    </nav>
  </header>

  <div class="frame-line frame-top-left"></div>
  <div class="frame-line frame-top-right"></div>
  <div class="frame-line frame-left"></div>
  <div class="frame-line frame-right"></div>
  <div class="frame-line frame-bottom-left"></div>
  <div class="frame-line frame-bottom-right"></div>

  <section class="hero" role="img" aria-label="Evening photo of the bar's white boat-shaped entrance with a red neon cocktails sign and greenery">
    <div class="hero-copy">
      <h1 class="hero-title">Velvet Den: A home away from home for&nbsp; the local community.</h1>
      <p class="hero-text">At Velvet Den, it is our goal to make sure that you enjoy every moment in your experience. Consider us your liaisons to happiness...</p>
      <a class="hero-button" href="#">TABLE RESERVATIONS</a>
    </div>
  </section>

  <div class="social">
    <a href="#"><span class="social-dot"></span>FOLLOW ON PAGEBOOK</a>
    <a href="#"><span class="social-dot"></span>FOLLOW ON CHIRPER</a>
    <a href="#"><span class="social-dot"></span>FOLLOW ON SNAPGRAM</a>
  </div>

  <div class="party-band">
    <span>Want to Book a Private Party?</span>
    <a href="#">Check Out Our Events Deck</a>
  </div>

  <footer class="site-footer">48 Harbor Lane Bayview, California 90210 info@velvetdenkx.com</footer>
</body>
</html>
```